Korimet Business Cards

Korimet is a software startup and we are looking for business cards that help convey our employee personalities, as well as the professionalism of the company.
Our company font is Comfortaa - and the company logo is attached (we are okay having the text beside the logo if applicable) where we can find the company colour scheme. Cards can be horizontal or vertical format.
We are looking for a two sided business card - on the front we will see the personal details of the employee (name, position, email and phone number), and then on the back, we will see the business details (name and logo, address, phone number, website, email, company tagline: "Accelerating technology disruption in the automotive market")
We want the design to be clean and simple, but also fun, modern, and capturing of a young startup vibe.

```html
<!DOCTYPE html>
<html lang="en">
<head>
<meta charset="utf-8">
<title>Korimet Business Cards</title>
<link rel="stylesheet" href="https://fonts.googleapis.com/css2?family=Comfortaa:wght@700&family=Arimo:wght@400;700&display=swap">
<style>
  :root {
    --backdrop: #2b2b2d;
    --card-light: #ffffff;
    --card-dark: #1b1b1d;
    --pattern-light: #ececef;
    --pattern-dark: #232326;
    --brand-violet: #5a3cc0;
    --brand-magenta: #c43fb0;
    --ink-dark: #222226;
    --ink-light: #f4f4f6;
    --rule-dark: #444448;
    --rule-light: #d8d8dc;
  }
  * { box-sizing: border-box; margin: 0; padding: 0; }
  html, body { width: 1200px; height: 1108px; overflow: hidden; }
  body {
    background: var(--backdrop);
    position: relative;
    font-family: "Arimo", Arial, sans-serif;
  }
  .card {
    position: absolute;
    width: 420px;
    height: 680px;
    border-radius: 26px;
    overflow: hidden;
    text-align: center;
  }
  .card-pattern { position: absolute; inset: 0; }
  .card--front { left: 120px; top: 190px; background: var(--card-light); color: var(--ink-dark); }
  .card--front .card-pattern { background: radial-gradient(circle at 50% 40%, var(--card-light) 0%, var(--pattern-light) 100%); }
  .card--back { left: 660px; top: 250px; background: var(--card-dark); color: var(--ink-light); }
  .card--back .card-pattern { background: radial-gradient(circle at 50% 40%, var(--pattern-dark) 0%, var(--card-dark) 100%); }
  .card-content {
    position: relative;
    display: flex;
    flex-direction: column;
    align-items: center;
    width: 100%;
    height: 100%;
  }
  .brand {
    margin-top: 150px;
    display: flex;
    align-items: center;
    gap: 14px;
  }
  .brand-dot {
    width: 22px; height: 22px; border-radius: 50%;
    background: var(--brand-violet);
  }
  .brand-name {
    font-family: "Comfortaa", "Arimo", sans-serif;
    font-weight: 700;
    font-size: 62px;
    color: var(--brand-violet);
    letter-spacing: -1px;
  }
  .person { margin-top: 150px; }
  .person-name {
    font-family: "Comfortaa", "Arimo", sans-serif;
    font-weight: 700;
    font-size: 30px;
    color: var(--brand-violet);
    letter-spacing: 1px;
    text-transform: uppercase;
  }
  .person-role { margin-top: 8px; font-size: 22px; }
  .rule { width: 110px; height: 1px; margin: 18px auto; background: var(--rule-dark); }
  .card--back .rule { background: var(--rule-light); }
  .contact-line { font-size: 22px; line-height: 1.4; }
  .address { margin-top: 70px; }
  .tagline {
    font-size: 22px;
    font-weight: 700;
    line-height: 1.25;
    color: var(--brand-magenta);
    text-transform: uppercase;
    letter-spacing: 0.5px;
  }
</style>
</head>
<body>
  <section class="card card--front" aria-label="Business card front">
    <div class="card-pattern" role="img" aria-label="Faint repeating brand pattern on white"></div>
    <div class="card-content">
      <div class="brand">
        <span class="brand-dot"></span>
        <span class="brand-name">Korimet</span>
      </div>
      <div class="person">
        <p class="person-name">Daniel Hartwell</p>
        <p class="person-role">Managing Director</p>
        <div class="rule"></div>
        <p class="contact-line">044-555 010 234</p>
        <p class="contact-line">hello@korimet.io</p>
        <p class="contact-line">www.korimet.io</p>
      </div>
    </div>
  </section>

  <section class="card card--back" aria-label="Business card back">
    <div class="card-pattern" role="img" aria-label="Faint repeating brand pattern on black"></div>
    <div class="card-content">
      <div class="brand">
        <span class="brand-dot"></span>
        <span class="brand-name">Korimet</span>
      </div>
      <div class="address">
        <p class="contact-line">17, Harbour Lane Studios</p>
        <p class="contact-line">80217, Northland</p>
      </div>
      <div class="rule"></div>
      <p class="contact-line">044-555 010 234</p>
      <p class="contact-line">hello@korimet.io</p>
      <p class="contact-line">www.korimet.io</p>
      <div class="rule"></div>
      <p class="tagline">Accelerating technology<br>disruption in<br>the automotive market</p>
    </div>
  </section>
</body>
</html>
```